Business cards for education company

We need a business card design for a relatively new company based in Queensland and operating across Australia. We resell diploma level education courses which include Business, Management, Finance, Community Services & Government courses. We offer over 20 different courses.
The target market is for anyone 16 years of age and older. There is no age limit.

We would like to see the design use the color blue and silver. The final design should communicate professionalism and a bright future.

We sell education but are also promoting the career they see themselves in 2-3 years in the future

Our company logo is attached.

Target Market(s)

We target all age groups above 16 years of age. The main target market would be people aged between 17-35.

We focus on those people who cannot make it into University or do not want to commit the time to a full degree.

Industry/Entity Type

Education

Requirements
Must have
• Professional
Company logo
website
Contact details:

Please use the following example:

Lionel Parfitt
Senior Education Consultant
0417 386 591
Lionel.parfitt@brightwaylearninghub.com.au
www.brightwaylearninghub.com.au

```html
<!DOCTYPE html>
<html lang="en">
<head>
<meta charset="utf-8">
<title>Brightway Learning Hub – Business Card</title>
<link href="https://fonts.googleapis.com/css2?family=Arimo:wght@400;700&display=swap" rel="stylesheet">
<style>
  :root {
    --backdrop: #1f5a35;
    --card-white: #ffffff;
    --band-silver: #c9cacc;
    --ink: #1a1a1a;
    --brand-navy: #1d3f86;
    --brand-blue: #2b6cc4;
    --accent-blue: #4a8fd6;
    --stripe-blue: #5a7fc4;
  }
  html, body {
    margin: 0;
    padding: 0;
    width: 1200px;
    height: 960px;
    overflow: hidden;
    background: var(--backdrop);
    font-family: "Arimo", Arial, sans-serif;
  }
  .business-card {
    position: absolute;
    left: 100px;
    top: 205px;
    width: 1000px;
    height: 550px;
    background: var(--card-white);
    box-shadow: 0 6px 18px rgba(0,0,0,0.35);
    overflow: hidden;
  }
  .title-band {
    position: absolute;
    left: 0; top: 0;
    width: 100%;
    height: 58px;
    background: var(--band-silver);
  }
  .band-mark {
    position: absolute;
    left: 0; top: 28px;
  }
  .holder {
    position: absolute;
    left: 40px; top: 28px;
    font-size: 23px;
    color: var(--ink);
    white-space: nowrap;
    line-height: 26px;
  }
  .holder .surname { color: var(--accent-blue); }
  .holder .divider {
    display: inline-block;
    width: 3px;
    height: 24px;
    background: var(--brand-blue);
    vertical-align: -4px;
    margin: 0 6px 0 8px;
  }
  .holder .divider.end { margin: 0 0 0 8px; }
  .website {
    position: absolute;
    right: 26px; top: 6px;
    font-size: 20px;
    color: var(--ink);
  }
  .brand {
    position: absolute;
    left: 150px; top: 150px;
    width: 700px;
    height: 160px;
    display: flex;
    align-items: center;
    gap: 34px;
  }
  .brand-dot {
    flex: none;
    width: 130px;
    height: 130px;
    border-radius: 50%;
    background: var(--brand-blue);
  }
  .brand-name {
    margin: 0;
    font-weight: 700;
    color: var(--brand-navy);
    text-transform: uppercase;
    line-height: 1.05;
  }
  .brand-name .line-main { display: block; font-size: 70px; letter-spacing: 1px; }
  .brand-name .line-sub { display: block; font-size: 38px; letter-spacing: 2px; }
  .stripes { position: absolute; }
  .stripes.left { left: 65px; top: 374px; }
  .stripes.right { left: 400px; top: 374px; }
  .contact {
    position: absolute;
    left: 410px;
    font-size: 21px;
    color: var(--ink);
    display: flex;
    align-items: center;
    gap: 16px;
  }
  .contact.email { top: 410px; }
  .contact.phone { top: 452px; font-size: 26px; }
  .contact svg { flex: none; }
</style>
</head>
<body>
  <div class="business-card">
    <div class="title-band">
      <svg class="band-mark" width="32" height="20" viewBox="0 0 32 20" aria-hidden="true">
        <rect x="0" y="2" width="32" height="2" fill="var(--stripe-blue)"/>
        <rect x="0" y="8" width="32" height="2" fill="var(--stripe-blue)"/>
        <rect x="0" y="14" width="32" height="2" fill="var(--stripe-blue)"/>
      </svg>
      <div class="holder">Lionel <span class="surname">Parfitt</span><span class="divider"></span>Senior Education Consultant<span class="divider end"></span></div>
      <div class="website">www.brightwaylearninghub.com.au</div>
    </div>

    <div class="brand">
      <div class="brand-dot"></div>
      <h1 class="brand-name"><span class="line-main">Brightway</span><span class="line-sub">Learning Hub</span></h1>
    </div>

    <svg class="stripes left" width="205" height="22" viewBox="0 0 205 22" aria-hidden="true">
      <rect x="0" y="1" width="205" height="2.5" fill="var(--stripe-blue)"/>
      <rect x="0" y="7" width="205" height="2.5" fill="var(--stripe-blue)"/>
      <rect x="0" y="13" width="205" height="2.5" fill="var(--stripe-blue)"/>
      <rect x="0" y="19" width="205" height="2.5" fill="var(--stripe-blue)"/>
    </svg>
    <svg class="stripes right" width="600" height="22" viewBox="0 0 600 22" aria-hidden="true">
      <rect x="0" y="1" width="600" height="2.5" fill="var(--stripe-blue)"/>
      <rect x="0" y="7" width="600" height="2.5" fill="var(--stripe-blue)"/>
      <rect x="0" y="13" width="600" height="2.5" fill="var(--stripe-blue)"/>
      <rect x="0" y="19" width="600" height="2.5" fill="var(--stripe-blue)"/>
    </svg>

    <div class="contact email">
      <svg width="34" height="24" viewBox="0 0 34 24" aria-hidden="true">
        <rect x="1" y="1" width="32" height="22" rx="2" fill="var(--brand-blue)" stroke="var(--brand-navy)" stroke-width="2"/>
        <polyline points="2,3 17,14 32,3" fill="none" stroke="var(--brand-navy)" stroke-width="2"/>
      </svg>
      <span>Lionel.parfitt@brightwaylearninghub.com.au</span>
    </div>
    <div class="contact phone">
      <svg width="32" height="32" viewBox="0 0 32 32" aria-hidden="true">
        <circle cx="16" cy="16" r="14.5" fill="var(--accent-blue)" stroke="var(--brand-navy)" stroke-width="2"/>
        <path d="M12 8 c-3 2 -3 6 -1 10 c2 4 5 7 9 7 l2 -3 l-3 -3 l-2 1 c-2 -1 -4 -4 -4 -6 l2 -1 l-1 -4 z" fill="var(--brand-navy)"/>
      </svg>
      <span>0417 386 591</span>
    </div>
  </div>
</body>
</html>
```